Veltrano Energy Business Card Design

website: www.veltranoenergy.example
Project: Business Card Design for Veltrano Energy
Name: Dorian Kettle
Title: Founder / Operations Strategist
Visual Identity & Logo:
Logo File: VEL-Logo-FullGradient-Final.png (Attached).
Color Palette: The brand relies on a distinctive Cyan (Blue) to Lime Green gradient.
Background Preference: We want a Dark Mode aesthetic (Deep Matte Black, Charcoal, or Dark Slate) to make the neon gradient of the logo pop. This feels more "tech/industrial" than a standard white card.
Design Aesthetic (The "Ops" Vibe):
Concept: "Grid & Infrastructure." We are a solar rental company, focusing on logistics and access.
Typography: White, bold sans-serif text for contact info. High contrast against the dark background.
Accents: Use the Cyan or Lime Green from the logo for thin divider lines or edge painting.
Avoid: No orange/gold (clashes with logo). No cartoon leaves.
Layout Requirements:
Front: Large, centered logo. Maybe a subtle UV gloss spot varnish over the logo icon.
Back: Name, Title, Contact Info.
Texture: Matte finish cardstock with gloss elements.
sample mock up of information on card: https://brivomarkco-my.filehost.example/:i:/g/personal/dorian_kettle_veltranoenergy_example/AbCdEfGhIjKlMnOpQrStUvWxYz012345678?e=Xy12Ab
Logo: https://brivomarkco.filehost.example/:i:/s/VeltranoEnergy/ZyXwVuTsRqPoNmLkJiHgFeDcBa9876543210?e=Pq34Cd

```html
<!DOCTYPE html>
<html lang="en">
<head>
<meta charset="utf-8">
<title>Veltrano Energy Business Card</title>
<link href="https://fonts.googleapis.com/css2?family=Montserrat:wght@400;500;700&display=swap" rel="stylesheet">
<style>
  :root {
    --stage: #2b2b2d;
    --card: #1c1c1d;
    --card-edge: #262628;
    --white: #f4f5f6;
    --muted: #d9dbde;
    --cyan: #1aa7d9;
    --teal: #1bbdc9;
    --lime: #a6cf3a;
  }
  * { margin: 0; padding: 0; box-sizing: border-box; }
  html, body { width: 1200px; height: 875px; overflow: hidden; }
  body {
    background: var(--stage);
    font-family: "Montserrat", sans-serif;
    color: var(--white);
    display: flex;
    align-items: center;
    justify-content: center;
    gap: 40px;
  }
  .card {
    position: relative;
    width: 540px;
    height: 309px;
    background: var(--card);
    border: 1px solid var(--card-edge);
    border-radius: 22px;
    overflow: hidden;
  }

  /* Front */
  .card-front {
    display: flex;
    flex-direction: column;
    align-items: center;
    justify-content: center;
    gap: 26px;
  }
  .brand {
    display: flex;
    align-items: center;
    gap: 14px;
  }
  .brand-mark {
    width: 40px;
    height: 40px;
    background: var(--cyan);
    border-radius: 4px;
  }
  .brand-name {
    font-weight: 500;
    font-size: 40px;
    letter-spacing: 0.5px;
    color: var(--teal);
  }
  .tagline {
    font-weight: 700;
    font-size: 15px;
    letter-spacing: 0.3px;
    color: var(--white);
  }

  /* Back */
  .card-back { padding: 30px 34px; }
  .card-back .brand { gap: 10px; }
  .card-back .brand-mark { width: 24px; height: 24px; border-radius: 3px; }
  .card-back .brand-name { font-size: 24px; }
  .feature-block {
    position: absolute;
    top: 34px;
    right: 40px;
    width: 130px;
    height: 130px;
    border-radius: 10px;
    background: linear-gradient(135deg, var(--teal), var(--cyan));
  }
  .region-badges {
    position: absolute;
    top: 182px;
    right: 40px;
    display: flex;
    gap: 6px;
  }
  .region-badge {
    width: 24px;
    height: 16px;
    border-radius: 2px;
    background: var(--muted);
  }
  .person { margin-top: 22px; }
  .person-name {
    font-size: 22px;
    color: var(--cyan);
    line-height: 1.1;
  }
  .person-name .first { font-weight: 700; }
  .person-name .last { font-weight: 400; }
  .person-title {
    font-weight: 500;
    font-size: 12px;
    color: var(--white);
    margin-top: 4px;
  }
  .contact {
    margin-top: 16px;
    display: grid;
    grid-template-columns: 16px auto;
    column-gap: 8px;
    row-gap: 3px;
    font-size: 12px;
    font-weight: 500;
    line-height: 1.35;
  }
  .contact-icon { width: 13px; height: 13px; margin-top: 2px; }
  .contact-icon path, .contact-icon circle { fill: none; stroke: var(--lime); stroke-width: 1.6; }
  .slogan {
    position: absolute;
    left: 34px;
    bottom: 26px;
    font-weight: 700;
    font-size: 14px;
    color: var(--teal);
  }
</style>
</head>
<body>

  <section class="card card-front">
    <div class="brand">
      <span class="brand-mark"></span>
      <span class="brand-name">Veltrano Energy</span>
    </div>
    <p class="tagline">Rent Solar. Generate Power. Save Smarter</p>
  </section>

  <section class="card card-back">
    <div class="feature-block"></div>
    <div class="region-badges">
      <span class="region-badge"></span>
      <span class="region-badge"></span>
      <span class="region-badge"></span>
    </div>

    <div class="brand">
      <span class="brand-mark"></span>
      <span class="brand-name">Veltrano Energy</span>
    </div>

    <div class="person">
      <p class="person-name"><span class="first">Dorian</span> <span class="last">Kettle</span></p>
      <p class="person-title">Founder / Operations Strategist</p>
    </div>

    <div class="contact">
      <svg class="contact-icon" viewBox="0 0 16 16"><path d="M3 2h3l1.5 3.5-2 1.2a8 8 0 0 0 3.8 3.8l1.2-2L14 10v3a1 1 0 0 1-1 1A11 11 0 0 1 2 3a1 1 0 0 1 1-1z"/></svg>
      <span>555.014.2280</span>
      <svg class="contact-icon" viewBox="0 0 16 16"><circle cx="8" cy="8" r="6.5"/><path d="M1.5 8h13M8 1.5c2 2 2 11 0 13M8 1.5c-2 2-2 11 0 13"/></svg>
      <span>www.veltranoenergy.example</span>
      <span></span>
      <span>2140 Harbor Mill Road<br>Fairhaven, FL 32000</span>
    </div>

    <p class="slogan">No debt, no liens, no maintenance, just savings</p>
  </section>

</body>
</html>
```